Plakat-Design für Dienstleister in den Bereichen Einbruchschutz, Schließsysteme und Zutrittslösungen
Zielgruppe
Seit über 58 Jahren sind wir als Familienunternehmen Brenni Riegeltechnik AG in Luzern und Zug bekannt für kompetente Dienstleistungen in den Bereichen Einbruchschutz, Schliesssysteme und Zutrittslösungen. Die Brenni Riegeltechnik AG ist einer der führenden Dienstleister für Schliesssysteme, Einbruchschutz und Tresore in der Zentralschweiz. Das Unternehmen ist seit über 58 Jahren in der Zentralschweiz verankert und beschäftigt aktuell an den beiden Standorten in Luzern und Zug 60 Mitarbeitende. In dieser Zeitspanne hat sich die Firma einen bekannten Namen für wirksame Schliesssysteme, Sicherheitslösungen für Private, Gewerbe und Industrie schaffen können – insbesondere für Unternehmungen in den Branchen Immobilien, Spitäler, Heime, Banken, Versicherungen, Öffentliche Einrichtungen, Institutionen, Behörden, Militär, Schulen, Universitäten, Sport, Kultur, Freizeit, Hotels sowie Jugendherbergen.
Plakat/Symbolik für weitere HR Marketing-Massnahmen - Führungsgrundsätze
Zielgruppe ist die bestehenden Mitarbeiter und zukünftigen Mitarbeiter. Es geht um 4 Führungsgrundsätze, welche dieses Jahr mit dem Kader und der Geschäftsleitung erarbeitet wurde, diese im Betrieb intern öffentlich aufzuzeigen und stets präsent zu haben. Aber auch für zukünftige potentielle neue Mitarbeiter soll es die Möglichkeit ergeben, offen über unsere Führungsgrundsätze zu informieren und transparent aufzuzeigen.
Aufgabenstellung
Es wurden 4 Führungsgrundsätze definiert; welche gestalterisch präsentiert werden sollen (intern - plakativ - Aufenthaltsraum, Toiletten,Treppenhaus, Deskophintergrund, Mitarbeiterbroschüre, Homepage, etc.)
-Perspektive ermöglichen
-Vertrauen & Sicherheit geben
-Miteinander wirken
-Freude erleben
Ergänzungen zu den vier Führungsgrundsätze von unserer Firma aus den Meeting siehe Anhang.
Ziel ist es, 2 Plakate zu haben: 1x alle 4 Grundsätze (Oberbegriffe) & je 1 Seite Plakat je Führungsgrundsatz mit den Ergänzungen.

```html
<!DOCTYPE html>
<html lang="de">
<head>
<meta charset="utf-8">
<title>4 Führungsgrundsätze – Brenni Riegeltechnik AG</title>
<link href="https://fonts.googleapis.com/css2?family=Bebas+Neue&family=Damion&family=Montserrat:wght@700&display=swap" rel="stylesheet">
<style>
:root{
  --header:#0096c0;
  --footer:#1ab8e2;
  --path-light:#93d4f5;
  --path-dark:#1ab0e6;
  --sky:#d6ecfa;
  --sky-deep:#a9dbf6;
  --blue:#0096c0;
  --tick-blue:#1296dc;
  --green:#7ab52a;
  --orange:#f0960f;
  --magenta:#e2007a;
  --ink:#1b1b2b;
  --white:#ffffff;
  --page:#f1f1f1;
  --footer-bar:#0088b8;
}
*{margin:0;padding:0;box-sizing:border-box}
html,body{width:1200px;height:1117px;overflow:hidden;background:var(--page)}
.poster{position:absolute;left:205px;top:0;width:789px;height:1117px;background:var(--white);overflow:hidden}
.poster-header{position:absolute;left:0;top:0;width:100%;height:115px;background:var(--header);display:flex;align-items:center;justify-content:center}
.poster-title{font-family:"Bebas Neue",sans-serif;font-size:88px;line-height:1;color:var(--white);letter-spacing:1px;padding-top:8px}
.skyline{position:absolute;background:linear-gradient(180deg,rgba(214,236,250,0) 0%,var(--sky) 45%,var(--sky-deep) 100%)}
.skyline-top{left:0;top:185px;width:475px;height:165px}
.skyline-bottom{left:230px;top:870px;width:559px;height:190px}
.skyline-right{left:520px;top:870px;width:269px;height:100px;background:linear-gradient(180deg,rgba(214,236,250,0),var(--sky))}
.route{position:absolute;left:0;top:0}
.illustration{position:absolute;border-radius:6px}
.illu-lookout{left:331px;top:132px;width:132px;height:210px;background:linear-gradient(180deg,#f39a44 0%,#f39a44 45%,#1d3f8c 46%,#1d3f8c 100%)}
.illu-handshake{left:300px;top:379px;width:173px;height:207px;background:linear-gradient(180deg,#1d3f8c 0%,#1d3f8c 55%,#f0963c 56%,#f0963c 100%)}
.illu-climb{left:320px;top:640px;width:143px;height:213px;background:linear-gradient(90deg,#ec6f52 0%,#ec6f52 50%,#222b57 51%,#222b57 100%)}
.illu-cheer{left:233px;top:880px;width:264px;height:176px;background:linear-gradient(180deg,#a9b8e6 0%,#a9b8e6 45%,#1d3f8c 46%,#1d3f8c 100%)}
.bubble{position:absolute;z-index:2;color:var(--white);text-align:center;display:flex;flex-direction:column;justify-content:center;align-items:center}
.bubble::after{content:"";position:absolute;width:44px;height:44px}
.bubble-name{font-family:"Bebas Neue",sans-serif;font-size:42px;line-height:.9}
.bubble-verb{font-family:"Damion",cursive;font-size:30px;line-height:1;margin-top:-2px}
.bubble-perspektive{left:55px;top:202px;width:266px;height:105px;background:var(--blue);border-radius:44px 52px 52px 0}
.bubble-perspektive::after{left:0;top:100%;background:radial-gradient(circle at 100% 100%,transparent 43px,var(--blue) 44px)}
.bubble-vertrauen{left:475px;top:405px;width:267px;height:105px;background:var(--green);border-radius:52px 44px 0 52px}
.bubble-vertrauen::after{right:0;top:100%;width:48px;background:radial-gradient(circle at 0 100%,transparent 43px,var(--green) 44px)}
.bubble-vertrauen .bubble-name{font-size:38px}
.bubble-miteinander{left:48px;top:630px;width:266px;height:105px;background:var(--orange);border-radius:44px 52px 52px 0}
.bubble-miteinander::after{left:0;top:100%;background:radial-gradient(circle at 100% 100%,transparent 43px,var(--orange) 44px)}
.bubble-freude{left:512px;top:963px;width:230px;height:105px;background:var(--magenta);border-radius:52px 44px 0 52px}
.bubble-freude::after{right:0;top:100%;width:48px;height:34px;background:radial-gradient(circle at 0 100%,transparent 43px,var(--magenta) 44px)}
.principles{position:absolute;list-style:none;font-family:"Montserrat",sans-serif;font-weight:700;font-size:11.4px;line-height:14.9px;color:var(--ink);letter-spacing:.3px;white-space:nowrap}
.principles li{position:relative;padding-left:27px;margin-bottom:14px}
.principles li::before{content:"";position:absolute;left:0;top:1.5px;width:12px;height:12px;border-radius:50%;background:var(--tick)}
.principles li::after{content:"";position:absolute;left:3px;top:4px;width:6px;height:3.5px;border-left:1.6px solid var(--white);border-bottom:1.6px solid var(--white);transform:rotate(-45deg)}
.list-perspektive{left:474px;top:154px;--tick:var(--tick-blue)}
.list-vertrauen{left:60px;top:394px;--tick:var(--green)}
.list-miteinander{left:474px;top:648px;--tick:var(--orange)}
.list-freude{left:60px;top:900px;--tick:var(--magenta)}
.poster-footer{position:absolute;left:0;top:1056px;width:100%;height:61px;background:var(--footer)}
.footer-url{position:absolute;left:0;top:1080px;width:100%;text-align:center;font-family:"Montserrat",sans-serif;font-weight:700;font-size:15px;color:var(--white);letter-spacing:.3px}
.footer-bar{position:absolute;left:543px;top:1100px;width:213px;height:9px;border-radius:5px;background:var(--footer-bar)}
</style>
</head>
<body>
<main class="poster">
  <header class="poster-header"><h1 class="poster-title">4 FÜHRUNGSGRUNDSÄTZE</h1></header>

  <div class="skyline skyline-top" role="img" aria-label="Helle Stadtsilhouette im Hintergrund"></div>
  <div class="skyline skyline-right" role="img" aria-label="Helle Stadtsilhouette im Hintergrund"></div>
  <div class="skyline skyline-bottom" role="img" aria-label="Helle Stadtsilhouette im Hintergrund"></div>

  <svg class="route" width="789" height="1117" viewBox="0 0 789 1117" aria-hidden="true">
    <path d="M7 350 H694 A40 40 0 0 1 734 390 V552 A40 40 0 0 1 694 592 H97 A40 40 0 0 0 57 632 V821 A40 40 0 0 0 97 861 H596 A30 30 0 0 1 626 891 V935" fill="none" stroke="var(--path-light)" stroke-width="17"/>
    <path d="M7 350 H694 A40 40 0 0 1 734 390 V552 A40 40 0 0 1 694 592 H97 A40 40 0 0 0 57 632 V821 A40 40 0 0 0 97 861 H596 A30 30 0 0 1 626 891 V935" fill="none" stroke="var(--path-dark)" stroke-width="3"/>
    <path d="M606 936 H646 L626 956 Z" fill="var(--path-light)"/>
    <path d="M614 939 H638 L626 951 Z" fill="var(--path-dark)"/>
  </svg>

  <section class="principle">
    <div class="illustration illu-lookout" role="img" aria-label="Illustration: Geschäftsmann blickt durch ein Fernrohr in die Ferne"></div>
    <div class="bubble bubble-perspektive"><span class="bubble-name">PERSPEKTIVE</span><span class="bubble-verb">ermöglichen</span></div>
    <ul class="principles list-perspektive">
      <li>WIR FORDEN DIE INDIVIDUELLE<br>ENTWICKLUNGUNSERER</li>
      <li>MITARBEITERWIR VERMITTEN UNSER<br>WISSEN AND KNOW-HOW</li>
      <li>WIR SIND OFFEN FUR NEUES</li>
      <li>WIR SETZEN UNS FUR DAS<br>WOHLBEFINDEN<br>UNSERERMITARBEITER EIN</li>
    </ul>
  </section>

  <section class="principle">
    <ul class="principles list-vertrauen">
      <li>WIR KOMMUNIZIEREN OFFEN,<br>DIREKT UND EHRLICH</li>
      <li>WIR SICHERN<br>ARBEITSPLATZE DURCH<br>WIRSHAFTLICHESARBEITEN</li>
      <li>WIR FORDEN EIGENINITIATIVE</li>
      <li>WIR LERNEN AUS UNSEREN<br>FEHLERN</li>
    </ul>
    <div class="illustration illu-handshake" role="img" aria-label="Illustration: zwei Geschäftsleute mit Aktentaschen geben sich die Hand"></div>
    <div class="bubble bubble-vertrauen"><span class="bubble-name">VERTRAUEN<br>&amp; SICHERHEIT</span><span class="bubble-verb">geben</span></div>
  </section>

  <section class="principle">
    <div class="illustration illu-climb" role="img" aria-label="Illustration: drei Personen helfen sich gegenseitig auf Stufen hinauf"></div>
    <div class="bubble bubble-miteinander"><span class="bubble-name">MITEINANDER</span><span class="bubble-verb">wirken</span></div>
    <ul class="principles list-miteinander">
      <li>ALLE WIRKEN MIT!</li>
      <li>WIR PFLEGEN EINEN<br>WERSCHATZENDER FAIREN<br>UMGANG</li>
      <li>WIR UNTERSTUTZEN EINANDER</li>
      <li>HERAUSFORDERNDE SITUATIONEN<br>MEISTERN WIRZUSAMMEN</li>
    </ul>
  </section>

  <section class="principle">
    <ul class="principles list-freude">
      <li>WIR ERSCHAFFFEN<br>ERFOLGSERLENISSE</li>
      <li>WIR FEIERN ERFOLGE</li>
      <li>WIR LASSEN<br>FREIRAUMFUR SPASS</li>
      <li>ZUSSAMMEN LACHEN</li>
    </ul>
    <div class="illustration illu-cheer" role="img" aria-label="Illustration: vier jubelnde Mitarbeitende feiern gemeinsam"></div>
    <div class="bubble bubble-freude"><span class="bubble-name">FREUDE</span><span class="bubble-verb">erleben</span></div>
  </section>

  <footer>
    <div class="poster-footer"></div>
    <p class="footer-url">www.brenni-riegel.ch</p>
    <div class="footer-bar"></div>
  </footer>
</main>
</body>
</html>
```